Business Card Design needed for logo design project

This project is linked to Brindell mechanical industry.

Our company needs a Business Card Design. Please refer to our original project in the link above.

Business

```html
<!DOCTYPE html>
<html lang="en">
<head>
<meta charset="utf-8">
<title>Brindell – Business Cards</title>
<link href="https://fonts.googleapis.com/css2?family=Open+Sans:wght@400;600;700&display=swap" rel="stylesheet">
<style>
  :root {
    --brand-red: #d10a0a;
    --brand-red-dark: #b90000;
    --paper: #ffffff;
    --ink: #555555;
    --rule: #444444;
    --backdrop: #e9e7e4;
  }
  * { margin: 0; padding: 0; box-sizing: border-box; }
  html, body {
    width: 1200px; height: 997px; overflow: hidden;
    background: var(--backdrop);
    font-family: "Open Sans", Arial, sans-serif;
  }
  .stage {
    position: relative; width: 1200px; height: 997px;
    display: flex; align-items: center; justify-content: center; gap: 60px;
  }
  .card {
    position: relative; width: 525px; height: 300px;
    box-shadow: 0 6px 18px rgba(0,0,0,0.12);
  }
  /* Front */
  .card--front {
    background: radial-gradient(ellipse at 45% 40%, var(--brand-red) 0%, var(--brand-red-dark) 100%);
    display: flex; flex-direction: column; align-items: center; justify-content: center;
    color: var(--paper);
  }
  .brand {
    display: flex; align-items: center; gap: 10px;
    font-weight: 700; font-size: 40px; letter-spacing: 1px; text-transform: uppercase;
  }
  .brand__dot { width: 22px; height: 22px; border-radius: 50%; background: currentColor; }
  .front__web {
    margin-top: 46px; display: flex; align-items: center; gap: 10px;
    font-size: 12px; letter-spacing: 3px;
  }
  .front__web::before, .front__web::after {
    content: ""; width: 44px; height: 1px; background: rgba(255,255,255,0.8);
  }
  /* Back */
  .card--back { background: var(--paper); color: var(--ink); }
  .back__brand {
    position: absolute; left: 36px; top: 112px;
    color: var(--brand-red); font-size: 32px;
  }
  .back__brand .brand__dot { width: 18px; height: 18px; }
  .person { position: absolute; right: 32px; top: 30px; text-align: right; }
  .person__name { color: var(--brand-red); font-size: 15px; font-weight: 600; }
  .person__title { font-size: 11px; margin-top: 2px; }
  .rule { position: absolute; height: 1px; background: var(--rule); }
  .rule--top { right: 32px; top: 78px; width: 330px; }
  .rule--bottom { left: 36px; top: 184px; width: 300px; }
  .address {
    position: absolute; right: 32px; top: 112px; text-align: right;
    font-size: 11px; line-height: 1.45;
  }
  .address__web { color: var(--brand-red); font-weight: 700; }
  .contacts {
    position: absolute; left: 36px; top: 200px; list-style: none;
    font-size: 12px; line-height: 1.35;
  }
  .contacts li { display: flex; align-items: center; gap: 8px; }
  .contacts svg { width: 11px; height: 11px; fill: var(--brand-red); }
</style>
</head>
<body>
<main class="stage">
  <section class="card card--front">
    <div class="brand"><span class="brand__dot"></span>Brindell</div>
    <div class="front__web">www.yourweb.com</div>
  </section>

  <section class="card card--back">
    <div class="brand back__brand"><span class="brand__dot"></span>Brindell</div>
    <div class="person">
      <div class="person__name">Daniel Reyes</div>
      <div class="person__title">Director</div>
    </div>
    <div class="rule rule--top"></div>
    <div class="address">
      Suite 102 Street name<br>
      State, Zip 2034,Country<br>
      <span class="address__web">www.yourweb.com</span>
    </div>
    <div class="rule rule--bottom"></div>
    <ul class="contacts">
      <li><svg viewBox="0 0 12 12"><path d="M1 4c0-2 2-3 5-3s5 1 5 3H8.5V3h-5v1zM2 5h8l1 6H1z"/></svg>127 345 9876</li>
      <li><svg viewBox="0 0 12 12"><path d="M3 0h6v12H3zM4 1.5v8h4v-8z"/></svg>345 345 9876</li>
      <li><svg viewBox="0 0 12 12"><path d="M3 0h6v4H3zM1 4h10v5H9v3H3V9H1zM4 8v3h4V8z"/></svg>345 345 9876</li>
      <li><svg viewBox="0 0 12 12"><path d="M0 2h12v1L6 7 0 3zM0 4.5l6 4 6-4V10H0z"/></svg>info@yourname.com</li>
    </ul>
  </section>
</main>
</body>
</html>
```